Social Media Marketing website

Need website designed for social media marketing company BrightLoop.com
Do no currently have logo.
Pages:
Main
Services
Order
Contact
Please use dummy text for now. I will provide content to winner later to add.
Main page should clearly show the steps with some sort of graphic: Establish, Engage, Analyze.
Services provided (steps):
1) Establish social media presence
2) Social media management and advertising
3) Analyze and engage
Site should be simple, clean and attractive. Design examples:
http://plinkster.com/
http://www.quillbase.com/
http://www.harrowvalemq.com/
Be creative! It should not look like a template.
Updates
Updated examples.
Contact me for questions.
dave@brightloop.com
3) Analyze and engage
Advertising

```html
<!DOCTYPE html>
<html lang="en">
<head>
<meta charset="utf-8">
<title>BrightLoop Marketing</title>
<link rel="stylesheet" href="https://fonts.googleapis.com/css2?family=Arimo:wght@400;700&family=Tinos:wght@400;700&display=swap">
<style>
  :root {
    --orange: #f07a24;
    --orange-dark: #e0641a;
    --blue: #1a78c2;
    --blue-dark: #0a69b0;
    --ink: #111111;
    --nav-top: #6a6a6a;
    --nav-bottom: #2e2e2e;
    --footer: #4d4d4d;
    --footer-base: #000000;
    --card-border: #d4d4d4;
    --white: #ffffff;
    --link: #f7931e;
    --social: #3b6fb0;
  }
  * { box-sizing: border-box; margin: 0; padding: 0; }
  html, body { width: 1200px; height: 1200px; overflow: hidden; }
  body { position: relative; background: var(--white); font-family: "Tinos", "Times New Roman", serif; color: var(--ink); }

  .top-strip { position: absolute; left: 0; top: 0; width: 1200px; height: 10px; background: linear-gradient(#2c2c2c, #6b6b6b); }

  .brand { position: absolute; left: 40px; top: 36px; display: flex; align-items: center; gap: 16px; }
  .brand-dot { width: 70px; height: 70px; border-radius: 50%; background: var(--blue); }
  .brand-name { font-family: "Arimo", Arial, sans-serif; font-weight: 700; font-size: 44px; color: var(--ink); letter-spacing: 1px; }

  .account { position: absolute; top: 53px; right: 72px; display: flex; gap: 12px; }
  .account a { display: block; width: 109px; height: 43px; line-height: 43px; text-align: center; background: linear-gradient(var(--orange), var(--orange-dark)); color: var(--white); font-family: "Arimo", Arial, sans-serif; font-weight: 700; font-size: 16px; text-decoration: none; }

  .main-nav { position: absolute; left: 0; top: 142px; width: 1200px; height: 55px; background: linear-gradient(var(--nav-top), var(--nav-bottom)); }
  .main-nav ul { list-style: none; display: flex; height: 55px; align-items: center; padding-left: 0; }
  .main-nav li { color: var(--white); font-size: 19px; height: 55px; line-height: 55px; }
  .main-nav li.home { width: 172px; padding-left: 76px; border-right: 2px solid var(--white); height: 38px; line-height: 38px; }
  .main-nav li.services { width: 162px; padding-left: 38px; border-right: 2px solid var(--white); height: 38px; line-height: 38px; }
  .main-nav li.order { width: 138px; padding-left: 36px; border-right: 2px solid var(--white); height: 38px; line-height: 38px; }
  .main-nav li.contact { padding-left: 37px; height: 38px; line-height: 38px; }
  .social { position: absolute; top: 12px; left: 770px; display: flex; gap: 10px; }
  .social span { width: 28px; height: 28px; background: var(--social); border-radius: 3px; }
  .search { position: absolute; left: 889px; top: 10px; display: flex; }
  .search-field { width: 201px; height: 36px; background: var(--white); }
  .search-btn { width: 39px; height: 36px; background: var(--orange); }

  .hero-visual { position: absolute; left: 61px; top: 215px; width: 476px; height: 355px; background: radial-gradient(circle at 50% 40%, #ffffff 0%, #eef3f7 60%, #dde3e8 100%); }
  .hero-copy { position: absolute; left: 558px; top: 226px; width: 575px; }
  .hero-copy h1 { font-size: 28px; font-weight: 700; margin-bottom: 20px; }
  .hero-copy h1 .accent { color: var(--blue); }
  .hero-copy p { font-size: 19px; line-height: 25px; }
  .hero-copy .tagline { font-size: 21px; font-weight: 700; color: var(--blue); margin: 18px 0 16px; }
  .hero-copy .tagline q { quotes: none; }
  .hero-copy .tagline .mark { color: var(--ink); }
  .learn-more { position: absolute; left: 980px; top: 485px; width: 148px; height: 42px; line-height: 42px; text-align: center; background: linear-gradient(#1b87cf, var(--blue-dark)); color: var(--white); font-family: "Arimo", Arial, sans-serif; font-weight: 700; font-size: 16px; }

  .step { position: absolute; top: 565px; width: 343px; height: 285px; border: 1px solid var(--card-border); border-radius: 14px; background: linear-gradient(#f3f3f3, #ffffff 45%); }
  .step-1 { left: 62px; } .step-2 { left: 431px; } .step-3 { left: 799px; }
  .step-icon { position: absolute; left: 34px; top: 18px; width: 64px; height: 64px; }
  .step-title { position: absolute; left: 120px; top: 30px; font-family: "Arimo", Arial, sans-serif; }
  .step-title .num { display: block; color: var(--orange); font-weight: 700; font-size: 25px; line-height: 28px; }
  .step-title .name { display: block; font-size: 20px; line-height: 26px; color: var(--ink); }
  .step p { position: absolute; left: 27px; top: 102px; width: 290px; font-size: 15px; line-height: 19.5px; }

  .footer-links { position: absolute; left: 0; top: 888px; width: 1200px; height: 230px; background: var(--footer); }
  .footer-col { position: absolute; top: 44px; font-family: "Arimo", Arial, sans-serif; }
  .footer-col h3 { color: var(--white); font-size: 16px; font-weight: 700; margin-bottom: 18px; }
  .footer-col ul { list-style: none; }
  .footer-col li { color: var(--link); font-size: 16px; line-height: 24px; }

  .site-base { position: absolute; left: 0; top: 1118px; width: 1200px; height: 82px; background: var(--footer-base); }
  .base-brand { position: absolute; left: 52px; top: 26px; display: flex; align-items: center; gap: 8px; }
  .base-brand .brand-dot { width: 28px; height: 28px; background: #6d6d6d; }
  .base-brand .brand-name { font-size: 20px; color: #9a9a9a; }
  .legal { position: absolute; left: 261px; top: 33px; color: var(--white); font-family: "Arimo", Arial, sans-serif; font-size: 12px; letter-spacing: 0.5px; }
  .base-nav { position: absolute; left: 500px; top: 28px; display: flex; list-style: none; }
  .base-nav li { color: #cfcfcf; font-size: 15px; padding: 0 30px; border-right: 2px solid #cfcfcf; line-height: 22px; }
  .base-nav li:first-child { padding-left: 20px; }
  .base-nav li:last-child { border-right: none; }
  .base-social { position: absolute; left: 1030px; top: 28px; display: flex; gap: 10px; }
  .base-social span { width: 26px; height: 26px; background: var(--social); border-radius: 3px; }
</style>
</head>
<body>
  <div class="top-strip"></div>

  <header>
    <div class="brand"><span class="brand-dot"></span><span class="brand-name">BrightLoop</span></div>
    <nav class="account"><a href="#">SIGN UP</a><a href="#">LOGIN</a></nav>
  </header>

  <nav class="main-nav">
    <ul>
      <li class="home">HOME</li>
      <li class="services">SERVICES</li>
      <li class="order">ORDER</li>
      <li class="contact">CONTACT</li>
    </ul>
    <div class="social"><span></span><span></span><span></span></div>
    <div class="search">
      <div class="search-field"></div>
      <div class="search-btn">
        <svg width="39" height="36" viewBox="0 0 39 36"><circle cx="17" cy="15" r="8" fill="none" stroke="#fff" stroke-width="3.5"/><line x1="23" y1="21" x2="31" y2="29" stroke="#fff" stroke-width="5" stroke-linecap="round"/></svg>
      </div>
    </div>
  </nav>

  <div class="hero-visual" role="img" aria-label="Globe with laptops connected around it, showing social media screens"></div>
  <section class="hero-copy">
    <h1>Effective Social Media <span class="accent">Marketing Solutions</span></h1>
    <p>Lorem ipsum dolor sit amet, consectetur adipiscing elit suspendisse tristique dui eu massa dapibus vitae&nbsp; mollis. Duis in lacus risus, ullamcorper eget condimentum sed.</p>
    <p class="tagline"><span class="mark">“</span>Achieve Business Success in 3 easy steps<span class="mark">”</span></p>
    <p>Turpis vel tempor rutrum, urna ligula varius libero, nec facilisis und lacus est vel nulla. Cum sociis natoque penatibus et magnis dis quid parturient montes hendrerit ipsum.</p>
  </section>
  <a class="learn-more">LEARN MORE</a>

  <article class="step step-1">
    <svg class="step-icon" viewBox="0 0 64 64"><rect width="64" height="64" fill="#f07a24"/></svg>
    <div class="step-title"><span class="num">STEP 1</span><span class="name">ESTABLISH</span></div>
    <p>Lorem ipsum dolor sit amet, consectetur adipiscing elit. Suspendisse tristique dui eu massa dapibus vitae hendrerit ipsum mollis. Duis lacus risus, ullamcorper eget condi-mentum sed, consequat at nisl. Sed posuere dapibus neque vitae tincidunt. Nulla sed justo est.</p>
  </article>
  <article class="step step-2">
    <svg class="step-icon" viewBox="0 0 64 64"><rect width="64" height="64" fill="#e8601c"/><rect x="12" y="14" width="34" height="28" rx="2" fill="none" stroke="#fff" stroke-width="3"/><line x1="8" y1="48" x2="56" y2="48" stroke="#fff" stroke-width="4"/><path d="M20 36 a10 10 0 0 1 10 -10 M20 31 a5 5 0 0 1 5 -5" fill="none" stroke="#fff" stroke-width="2.5"/></svg>
    <div class="step-title"><span class="num">STEP 2</span><span class="name">ENGAGE</span></div>
    <p>Lorem ipsum dolor sit amet, consectetur adipiscing elit. Suspendisse tristique dui eu massa dapibus vitae hendrerit ipsum mollis. Duis lacus risus, ullamcorper eget condi-mentum sed, consequat at nisl. Sed posuere dapibus neque vitae tincidunt. Nulla sed justo est</p>
  </article>
  <article class="step step-3">
    <svg class="step-icon" viewBox="0 0 64 64"><rect width="64" height="64" fill="#f07a24"/><rect x="10" y="40" width="9" height="14" fill="#fff"/><rect x="22" y="32" width="9" height="22" fill="#fff"/><rect x="34" y="28" width="9" height="26" fill="#fff"/><rect x="46" y="20" width="9" height="34" fill="#fff"/><polyline points="10,30 24,20 34,24 52,8" fill="none" stroke="#fff" stroke-width="2.5"/></svg>
    <div class="step-title"><span class="num">STEP 3</span><span class="name">ANALYZE</span></div>
    <p>Lorem ipsum dolor sit amet, consectetur adipiscing elit. Suspendisse tristique dui eu massa dapibus vitae hendrerit ipsum mollis. Duis lacus risus, ullamcorper eget condi-mentum sed, consequat at nisl. Sed posuere dapibus neque vitae tincidunt. Nulla sed justo est</p>
  </article>

  <footer>
    <div class="footer-links">
      <div class="footer-col" style="left:150px"><h3>Lorem Ipsum Dolor</h3><ul><li>Lorem Ipsum Dolor</li><li>Nascetur ridiculus</li><li>Nascetur</li><li>Lorem Ipsum Dolor</li><li>Ridic</li></ul></div>
      <div class="footer-col" style="left:415px"><h3>Lorem Ipsum Dolor</h3><ul><li>Lorem Ipsum Dolor</li><li>Nascetur</li><li>Ridic</li></ul></div>
      <div class="footer-col" style="left:679px"><h3>Lorem Ipsum Dolor</h3><ul><li>Nascetur ridiculus</li><li>Nascetur</li><li>Lorem Ipsum Dolor</li><li>Ridic</li></ul></div>
      <div class="footer-col" style="left:943px"><h3>Lorem Ipsum Dolor</h3><ul><li>Lorem Ipsum Dolor</li><li>Nascetur ridiculus</li><li>Nascetur</li><li>Lorem Ipsum Dolor</li><li>Ridic</li></ul></div>
    </div>
    <div class="site-base">
      <div class="base-brand"><span class="brand-dot"></span><span class="brand-name">BrightLoop</span></div>
      <div class="legal">Privacy Policy | Sitemap</div>
      <ul class="base-nav"><li>HOME</li><li>SERVICES</li><li>ORDER</li><li>CONTACT</li></ul>
      <div class="base-social"><span></span><span></span><span></span></div>
    </div>
  </footer>
</body>
</html>
```